www.tlorvantix.com

We are a company that is in the business of extending the life of surgical equipment by repairing or refurbishing equipment to save hospitals, surgery centers and clinics money. We call ourselves Pelbrook Medical Corporation. We are in need of a website that delivers the "feel" of what of we do everyday. A website that explains our services but at the same time has a touch that is different from the rest. Many companies repair but their websites may not "pull" customers to inquire, we need that punch. At this time we are not looking for e-commerce but would like the option of adding that in the future. We do sell new and used equipment, so we like to be able to highlight those manufacturers on our site. We would like the website to have enough layouts for pictures to describe what we repair.
Target Market(s)
Biomedical Technicians and Managers, Hospital Purchasing Departments, OR Managers, type of facilities that our customer exists in, hospitals, surgery centers, clinics, animal hospitals
Industry/Entity Type
E-Commerce
Requirements
Must have
- An easy to navigate website, modern looking.
Easy to modify with pictures and or additional web pages
The winning designer to be available for future modifications and changes
Website to be unique compared to our competition, which are numerous
Nice to have
- E-Commerce capability

```html
<!DOCTYPE html>
<html lang="en">
<head>
<meta charset="utf-8">
<title>Pelbrook Medical Corporation — Repairing Equipments</title>
<link rel="stylesheet" href="https://fonts.googleapis.com/css2?family=Arimo:wght@400;700&display=swap">
<style>
:root{
  --yellow:#fde14b;
  --green:#0b6b5a;
  --green-light:#17806c;
  --navy:#172129;
  --panel:#ececec;
  --ring:#1ea3dc;
  --text:#1d1d1d;
  --muted:#8a8a8a;
  --white:#ffffff;
}
*{margin:0;padding:0;box-sizing:border-box}
html,body{width:701px;height:1200px;overflow:hidden}
body{font-family:"Arimo",Arial,sans-serif;color:var(--text);position:relative;
  background:linear-gradient(var(--yellow) 0 411px,var(--green) 411px 788px,var(--navy) 788px 1200px)}
.abs{position:absolute}
.brand{left:88px;top:50px}
.brand-name{font-size:20px;font-weight:700;letter-spacing:.5px}
.brand-tag{font-size:9px;font-weight:700;margin-top:6px}
.top-links{top:74px;left:476px;display:flex;gap:30px}
.top-links a{font-size:9px;font-weight:700;color:var(--text);text-decoration:none;border-bottom:1px solid var(--text);padding-bottom:3px}
.nav{left:74px;top:108px;width:537px;height:42px;background:var(--green);border-radius:10px 10px 0 0;display:flex;align-items:center}
.nav-home{width:24px;height:24px;border-radius:50%;background:var(--white);margin-left:26px;display:flex;align-items:center;justify-content:center}
.nav a{color:var(--white);font-size:11px;text-decoration:none;position:absolute;top:15px}
.hero{left:74px;top:150px;width:537px;height:258px;background:linear-gradient(135deg,#5d656b 0%,#c4cad0 35%,#2c4e8d 60%,#8f979e 100%)}
.hero-text{left:118px;top:252px;font-weight:700}
.hero-text .l1{font-size:32px;color:var(--white);letter-spacing:1px}
.hero-text .l2{font-size:15px;color:#2a9a82;margin:4px 0 0 32px}
.hero-text .l3{font-size:17px;color:var(--white);margin-top:4px}
.tile{top:415px;width:179px;height:80px}
.tile-1{left:74px;background:linear-gradient(135deg,#fbe25a,#e9c93a)}
.tile-2{left:253px;background:linear-gradient(135deg,#2b3a45,#1a252c)}
.tile-3{left:432px;background:var(--green)}
.map{left:520px;top:425px;width:70px;height:30px;border-radius:4px;background:rgba(255,255,255,.85)}
.tile-3-text{left:432px;top:463px;width:179px;text-align:center;color:var(--white);font-size:8px;font-weight:700}
.tile-3-text span{display:block;font-size:6px;margin-top:4px;padding-left:80px}
.strip{top:495px;height:25px;width:179px;display:flex;align-items:center;font-size:5.5px;font-weight:700;gap:6px;padding-left:8px}
.strip i{width:11px;height:11px;border-radius:50%;display:inline-block;flex:none}
.strip-1{left:74px;background:#62bba7;color:var(--white)}
.strip-1 i{background:var(--white)}
.strip-2{left:253px;background:#dedfe0;color:var(--text)}
.strip-2 i{background:var(--green)}
.strip-3{left:432px;background:#e6dfb8;color:var(--text)}
.strip-3 i{background:var(--yellow)}
.panel{left:74px;top:520px;width:537px;height:640px;background:var(--panel);border-radius:0 0 12px 12px}
.badge{width:40px;height:40px;border-radius:50%;background:var(--navy);display:flex;align-items:center;justify-content:center}
.section-title{width:537px;left:74px;text-align:center;color:var(--green);font-size:15px;font-weight:700}
.lead{left:112px;top:620px;width:460px;font-size:10px;line-height:16px;color:var(--muted)}
.social{top:690px;width:26px;height:26px;border-radius:50%;background:#b9b9b9;display:flex;align-items:center;justify-content:center}
.rule{top:744px;height:1px;width:130px;background:#b0b7bd}
.featured{left:74px;width:537px;top:780px;text-align:center;font-size:14px;color:var(--text)}
.arrows{left:534px;top:778px;width:30px;height:18px;background:#d4d7da;border-radius:3px;display:flex;justify-content:space-around;align-items:center}
.product-img{top:821px;width:88px;height:88px;border-radius:50%;border:4px solid var(--ring);background:linear-gradient(135deg,#54606a,#c5ccd2 55%,#2d5d8f)}
.product{top:919px;width:160px;text-align:center}
.product h3{font-size:14px;font-weight:700}
.product h3 small{font-size:7px}
.product .sub{font-size:7px;font-weight:700;margin-top:6px}
.product p{font-size:7.5px;line-height:10px;color:var(--muted);margin-top:6px}
.product p.big{font-size:11px;line-height:13px}
.foot-col{top:1067px;font-size:8px;line-height:13px}
.foot-col h4{font-size:10px;font-weight:700;margin-bottom:6px}
.foot-col h4.accent{color:var(--green)}
.copyright{left:0;width:701px;top:1173px;text-align:center;color:var(--white);font-size:7px;font-weight:700}
</style>
</head>
<body>

<header>
  <div class="abs brand">
    <div class="brand-name">PELBROOK</div>
    <div class="brand-tag">REPAIRING EQUIPMENTS</div>
  </div>
  <nav class="abs top-links"><a href="#">SITE MAP</a><a href="#">CONTACT US</a></nav>
</header>

<nav class="abs nav">
  <span class="nav-home">
    <svg width="12" height="12" viewBox="0 0 12 12"><path d="M6 1 L11 6 H9.5 V11 H7 V8 H5 V11 H2.5 V6 H1 Z" fill="#0b6b5a"/></svg>
  </span>
  <a href="#" style="left:58px">HOME</a>
  <a href="#" style="left:137px">ABOUT US</a>
  <a href="#" style="left:248px">SERVICES</a>
  <a href="#" style="left:348px">CONTACT US</a>
  <a href="#" style="left:452px">KINDS</a>
</nav>

<div class="abs hero" role="img" aria-label="Photo of polished surgical scissors and clamps on a blue surgical towel"></div>
<div class="abs hero-text">
  <div class="l1">REPAIRING</div>
  <div class="l2">THE EQUIPMENTS</div>
  <div class="l3">YOUR SLOGAN HERE</div>
</div>

<div class="abs tile tile-1" role="img" aria-label="Photo of surgical scissors on yellow"></div>
<div class="abs tile tile-2" role="img" aria-label="Photo of a medical technician in scrubs"></div>
<div class="abs tile tile-3"></div>
<div class="abs map" role="img" aria-label="World map silhouette"></div>
<div class="abs tile-3-text">WHERE CAN YOU CAN CONTACT US<span>LEARN MORE</span></div>

<div class="abs strip strip-1"><i></i>PLSE YOU CAN CONTACT US TO GET MORE DATA</div>
<div class="abs strip strip-2"><i></i>HOW TO KEEP WHAT I LIKE LEARN MORE</div>
<div class="abs strip strip-3"><i></i>OUR BEST OFFERS FOR THIS MONTH IN YOUR COUNTRY</div>

<main class="abs panel"></main>

<div class="abs badge" style="left:323px;top:536px">
  <svg width="18" height="18" viewBox="0 0 12 12"><path d="M6 1 L11 6 H9.5 V11 H7 V8 H5 V11 H2.5 V6 H1 Z" fill="#fff"/></svg>
</div>
<h2 class="abs section-title" style="top:589px">YOUR CHOICE EVEN WHAT IS OUR</h2>
<p class="abs lead">Bright Ladle sprouted from a hot dog cart in Corwin Square Park in Lindenport created by Ollie Varesk's Harrow Square Hospitality Group (HSHG) to support the Corwin Square Park Conservancy's first art installation. The cart was quite the success, with Ladle Fans lined up daily for three sum-</p>

<div class="abs social" style="left:492px">
  <svg width="14" height="10" viewBox="0 0 14 10"><rect x="0.5" y="0.5" width="13" height="9" fill="none" stroke="#fff"/><path d="M0.5 0.5 L7 6 L13.5 0.5" fill="none" stroke="#fff"/></svg>
</div>
<div class="abs social" style="left:520px"></div>
<div class="abs social" style="left:549px"></div>

<div class="abs rule" style="left:193px"></div>
<div class="abs badge" style="left:323px;top:724px">
  <svg width="18" height="16" viewBox="0 0 18 16"><path d="M2 6 H16 L14 15 H4 Z" fill="#fff"/><path d="M5 6 L9 1 L13 6" fill="none" stroke="#fff" stroke-width="1.5"/></svg>
</div>
<div class="abs rule" style="left:378px"></div>
<h2 class="abs featured">FEAURED PRODUCT</h2>
<div class="abs arrows">
  <svg width="5" height="8" viewBox="0 0 5 8"><path d="M4 1 L1 4 L4 7" fill="none" stroke="#fff" stroke-width="1.3"/></svg>
  <svg width="5" height="8" viewBox="0 0 5 8"><path d="M1 1 L4 4 L1 7" fill="none" stroke="#0b6b5a" stroke-width="1.3"/></svg>
</div>

<div class="abs product-img" style="left:138px" role="img" aria-label="Photo of surgical instruments"></div>
<div class="abs product-img" style="left:301px" role="img" aria-label="Photo of clamps on blue cloth"></div>
<div class="abs product-img" style="left:474px" role="img" aria-label="Photo of medical monitoring equipment"></div>

<section class="abs product" style="left:102px">
  <h3>AM <small>I ANY GOOD AT THIS?</small></h3>
  <p class="big">Yes, I wasn't always, how-<br>ever, I didn't know<br>Vicidkit.</p>
</section>
<section class="abs product" style="left:265px">
  <h3>MY CLIENTS</h3>
  <div class="sub">ARE LOCATED EVERYWHERE</div>
  <p>United States<br>Manila (Philippines)<br>Canada<br>India</p>
</section>
<section class="abs product" style="left:438px">
  <h3>MY CLIENTS</h3>
  <div class="sub">ARE LOCATED EVERYWHERE</div>
  <p>United States<br>Manila (Philippines)<br>Canada<br>India</p>
</section>

<div class="abs badge" style="left:323px;top:1004px">
  <svg width="20" height="20" viewBox="0 0 20 20"><circle cx="10" cy="10" r="6" fill="none" stroke="#fff" stroke-width="3" stroke-dasharray="3 2"/><circle cx="10" cy="10" r="2.5" fill="#fff"/></svg>
</div>

<footer>
  <div class="abs foot-col" style="left:135px"><h4>MENU</h4>HOME<br>ABOUT US<br>BEST OFFERS<br>WHY US</div>
  <div class="abs foot-col" style="left:231px"><h4 class="accent">PORDUCT'S SECTORS</h4>MEN<br>WOMEN<br>BOYS AND GIRLS<br>OUT OF CATEGORY</div>
  <div class="abs foot-col" style="left:380px"><h4>PORDUCT'S SECTORS</h4>MEN<br>WOMEN<br>BOYS AND GIRLS<br>OUT OF CATEGORY</div>
  <div class="abs foot-col" style="left:536px"><h4 class="accent">MENU</h4>HOME<br>ABOUT US<br>BEST OFFERS<br>WHY US</div>
  <div class="abs copyright">ALLCOPY RIGHTS RESERVED BY COMPANY NAME</div>
</footer>

</body>
</html>
```